Business Card Design Project

I need a business card design for an Organic drive thru coffee kiosk. We will serve organic coffee, teas & smoothies and will serve healthy breakfast food/snacks for people on the go.
I want the card to have 2-3 colors max (earthy colors like browns, greens and so on).
I have attached the logo I want used and would love to play off the theme of "balance."
Include:
Tidy-Kettle Coffee
address: 4820 Gorvin Ct. Raleigh, NC 27583
phone: 919-731-4062
website: www.tidy-kettle.com (website is not up yet but still include it on card)
email: Rosalind@tidy-kettle.com
I want one of the following sayings somewhere on the card (the front or back is fine):
"Break the fast with Tidy-Kettle"
"Break the fast with Tidy-Kettle"
Maybe on the back list what we offer:
-Organic coffee, espresso & tea
-Blendora smoothies & protein shakes
-Zesty Pour (100% fresh local fruit and veggies)
-Tender Nibs

```html
<!DOCTYPE html>
<html lang="en">
<head>
<meta charset="utf-8">
<title>Tidy-Kettle Coffee – Business Card</title>
<link rel="stylesheet" href="https://fonts.googleapis.com/css2?family=Open+Sans:wght@400;600&display=swap">
<style>
  :root {
    --backdrop: #121212;
    --band-light: #fdd29a;
    --band-mid: #e9b887;
    --band-edge: #c99b70;
    --brown-deep: #3f2415;
    --brown-dark: #2e1a0e;
    --back-centre: #2d190e;
    --back-edge: #1c0f08;
    --contact-ink: #eabb8c;
    --brand-ink: #4a2916;
    --accent-bean: #a4532f;
    --tagline-ink: #6f5337;
    --shadow: rgba(0, 0, 0, 0.6);
  }
  * { margin: 0; padding: 0; box-sizing: border-box; }
  html, body {
    width: 903px;
    height: 1200px;
    overflow: hidden;
    background: var(--backdrop);
    font-family: "Open Sans", sans-serif;
  }
  .canvas { position: relative; width: 903px; height: 1200px; }

  .card {
    position: absolute;
    left: 130px;
    width: 645px;
    height: 368px;
    box-shadow: 0 8px 24px var(--shadow);
    overflow: hidden;
  }
  .card--front { top: 121px; }
  .card--back {
    top: 656px;
    height: 367px;
    background: radial-gradient(ellipse at 50% 45%, var(--back-centre) 0%, var(--back-edge) 100%);
    display: flex;
    align-items: center;
    justify-content: center;
  }

  .brand-band {
    height: 183px;
    background: radial-gradient(ellipse at 35% 20%, var(--band-light) 0%, var(--band-mid) 60%, var(--band-edge) 100%);
    display: flex;
    flex-direction: column;
    align-items: center;
    padding-top: 25px;
  }
  .brand-mark { width: 62px; height: 62px; }
  .brand-name {
    margin-top: 4px;
    font-size: 42px;
    font-weight: 600;
    line-height: 1;
    color: var(--brand-ink);
    letter-spacing: -0.5px;
  }
  .brand-descriptor {
    margin-top: 13px;
    font-size: 11px;
    font-weight: 600;
    letter-spacing: 1.6px;
    color: var(--accent-bean);
  }

  .contact-band {
    height: 185px;
    background: linear-gradient(180deg, var(--brown-deep) 0%, var(--brown-dark) 100%);
    padding-top: 31px;
    text-align: center;
    color: var(--contact-ink);
    font-size: 18.5px;
    line-height: 24.7px;
    font-style: normal;
  }

  .tagline {
    font-size: 31px;
    color: var(--tagline-ink);
    margin-top: -4px;
  }
</style>
</head>
<body>
  <main class="canvas">
    <section class="card card--front" aria-label="Card front">
      <header class="brand-band">
        <svg class="brand-mark" viewBox="0 0 62 62" aria-hidden="true">
          <circle cx="31" cy="31" r="30" fill="var(--accent-bean)"/>
        </svg>
        <div class="brand-name">Tidy-Kettle</div>
        <div class="brand-descriptor">ORGANIC COFFEE + CAFE</div>
      </header>
      <address class="contact-band">
        <div class="contact-line">Tidy-Kettle Coffee</div>
        <div class="contact-line">Address: 4820 Gorvin Ct. Raleigh, NC 27583</div>
        <div class="contact-line">Phone: 919-731-4062</div>
        <div class="contact-line">Website: www.tidy-kettle.com</div>
        <div class="contact-line">Email: Rosalind@tidy-kettle.com</div>
      </address>
    </section>

    <section class="card card--back" aria-label="Card back">
      <p class="tagline">Break the fast with Tidy-Kettle</p>
    </section>
  </main>
</body>
</html>
```